Premium Honey Fusions need a label design. 5 awesome blends (see below)

We need a label design for a line of honey. Brand is an existing brand called MELVORIN. www.melvorinusa.example
MELVORIN is a line of juices. The honey line is an extension of the MELVORIN juice line.
Blends are:
Honey Cinnamon
Honey Saffron
Honey Ginger
Honey Herbs
Honey Wild Flower
PRODUCT FROM INDIA
We need a label design for a line of honey. Brand is an existing brand called MELVORIN.
See www.melvorinusa.example
We would like to see label designs that:
-are easy to read, clean
-"Honey Cinnamon”, etc... should be prominent, as it will be what will set us apart.
-use colors that communicate "premium honey"
-premium
-unique
-healthy/good for you
-We need a “Help us save the bees” type message on the logo. We will give % of profit from sale of honey to go towards saving the bees.
The final design should communicate :
-healthy
-DELICIOUS!!!! (it is!)
-premium
-unique
-exotic
Glass bottle is square (see pics) and label has 3 sides:
Front panel
Side panel 1: will be nutritional, ingredients, UPC, etc
Side panel 2: a story about bees? about saffron, about cinnamon??
Target Market(s)
Hispanic and American markets.
Healthy conscious people.
Premium honey market
Look and feel

```html
<!DOCTYPE html>
<html lang="en">
<head>
<meta charset="UTF-8">
<title>MELVORIN Honey Cinnamon Label</title>
<link rel="stylesheet" href="https://fonts.googleapis.com/css2?family=Lobster&family=Josefin+Sans:wght@400;700&display=swap">
<style>
  :root {
    --page-bg: #efefef;
    --label-red: #e42d2f;
    --band-brown: #7b3f14;
    --label-edge: #5a2a10;
    --band-line: #fbeee0;
    --accent-orange: #f28a2a;
    --title-white: #ffffff;
    --seal-red: #b5162a;
    --seal-ring: #d8343f;
    --weight-text: #5a1c14;
  }
  html, body {
    margin: 0;
    padding: 0;
    width: 1200px;
    height: 1000px;
    overflow: hidden;
    background: var(--page-bg);
  }
  .canvas {
    position: relative;
    width: 1200px;
    height: 1000px;
  }
  .label {
    position: absolute;
    left: 387px;
    top: 172px;
    width: 426px;
    height: 656px;
  }
  .label-shape {
    position: absolute;
    inset: 0;
    width: 426px;
    height: 656px;
  }
  .brand-name {
    position: absolute;
    left: 0;
    right: 0;
    top: 84px;
    text-align: center;
    font-family: "Josefin Sans", sans-serif;
    font-weight: 700;
    font-size: 50px;
    letter-spacing: 1px;
    color: var(--title-white);
    margin: 0;
  }
  .product-title {
    position: absolute;
    left: 0;
    right: 0;
    top: 222px;
    margin: 0;
    text-align: center;
    transform: rotate(-4.5deg);
    font-family: "Lobster", cursive;
    font-weight: 400;
  }
  .product-title .origin,
  .product-title .flavour {
    display: block;
    color: var(--accent-orange);
    font-size: 36px;
    line-height: 1;
  }
  .product-title .honey {
    display: block;
    color: var(--title-white);
    font-size: 118px;
    line-height: 1.02;
  }
  .net-weight {
    position: absolute;
    left: 0;
    right: 0;
    top: 620px;
    margin: 0;
    text-align: center;
    font-family: "Josefin Sans", sans-serif;
    font-size: 22px;
    color: var(--weight-text);
  }
</style>
</head>
<body>
  <main class="canvas">
    <section class="label" aria-label="MELVORIN Honey Cinnamon front label">
      <svg class="label-shape" viewBox="0 0 426 656" xmlns="http://www.w3.org/2000/svg">
        <defs>
          <clipPath id="label-outline">
            <path d="M2 213 A211 211 0 0 1 424 213 L424 654 L2 654 Z"/>
          </clipPath>
        </defs>
        <g clip-path="url(#label-outline)">
          <rect class="label-body" x="0" y="0" width="426" height="656" fill="var(--label-red)"/>
          <polygon class="title-band" points="0,236 426,208 426,412 0,468" fill="var(--band-brown)"/>
          <line class="band-rule" x1="0" y1="226" x2="426" y2="198" stroke="var(--band-line)" stroke-width="4"/>
          <line class="band-rule" x1="0" y1="478" x2="426" y2="422" stroke="var(--band-line)" stroke-width="4"/>
        </g>
        <path d="M2 213 A211 211 0 0 1 424 213 L424 654 L2 654 Z" fill="none" stroke="var(--label-edge)" stroke-width="3"/>
        <g class="bee-seal" role="img" aria-label="Help us save the bees seal">
          <circle cx="213" cy="517" r="66" fill="var(--seal-red)"/>
          <circle cx="213" cy="517" r="48" fill="none" stroke="var(--seal-ring)" stroke-width="4"/>
        </g>
      </svg>
      <p class="brand-name">MELVORIN</p>
      <h1 class="product-title">
        <span class="origin">Made in India</span>
        <span class="honey">Honey</span>
        <span class="flavour">Cinnamon</span>
      </h1>
      <p class="net-weight">8oz. (226g)</p>
    </section>
  </main>
</body>
</html>
```